Vodka label, brand name: LATE BIRCH

We are looking for a vodka label design, which will print on paper or plastic (not a bottle printing)

We are small distilling company: Ferncliff Distillery. Located in Toronto, Canada. Our business is small batches of handcrafted very smooth vodka production. 40% abv. Made from cane sugar and spring water.

Our audience pretty mach everyone who consume vodka/alcohol, we are not targeting any specific group.

Back label should have barcode, government warning and this text:

Our vodka is handmade in small batches to the highest standards befitting the true vodka perfectionist. We use silk filtering process for exceptional purity, clarity, and smoothness. It is distilled 6 times from the finest organic cane sugar using only the best Canadian spring water. Discover the smooth, clear taste for yourself.
Distilled and Bottled by
Ferncliff Distillery Inc.
Toronto, Canada

Government Warning: In accordance to the Surgeon General, women should not drink alcoholic beverages during pregnancy because of the risk of birth defects. Consumption of alcoholic beverages impairs your ability to drive a car or operate machinery and may cause health problems.

Size of the bottle as follows (see example in the attachment) :
Volume: 750ml
Total height: 330mm
Body diameter: 77mm
Closure: Bar Top
Silver synthetic cork

Target Market(s)

Colors

Designer to choose colors to be used in the design.

Requirements
Must have
• Incorporate the name: LATE BIRCH
• Incorporate: DISTILLED FROM ORGANIC CANE SUGAR
• Back bottle label should have barcode, government warning and this text:
• Our vodka is handmade in small batches to the highest standards befitting the true vodka perfectionist. We use silk filtering process for exceptional purity, clarity, and smoothness. It is distilled 6 times from the finest organic cane sugar using only the best Canadian spring water. Discover the smooth, clear taste for yourself.
• Distilled and Bottleb by
• Ferncliff Distillery Inc.
• Toronto, Canada
• Government Warning: In accordance to the Surgeon General, women should not drink alcoholic beverages during pregnancy because of the risk of birth defects. Consumption of alcoholic beverages impairs your ability to drive a car or operate machinery and may cause health problems.
Nice to have
• 1) To show in wording or design it was Handmade
• 2) To show in wording or design it was made with Natural Spring Water
• To show in wording or design it was made in small batches
• 3) To show in wording or design it was made local in Toronto, Canada
• "The Six" "The 6ix"- is the nick name of city of Toronto that's just for designer to consider and not mandatory to implement on design
Should not have
• We try to lower cost of printing , so design should be for digital printing without Gold, Silver or any other color which requires foil application on label and will increase cost of printing.
• No copy paste from internet images. Such designs will be ignored and reported to website admin. Authentic design work only.
• Please try not to use clock or any related to that images. Its nothing to do with clock, its too naive to show 6 pm on the watches in your design. Its could be time of the day (evening), after work, the six as nick name of Toronto. But not clock or watches .

```html
<!DOCTYPE html>
<html lang="en">
<head>
<meta charset="utf-8">
<title>Late Birch Vodka – Label</title>
<link rel="stylesheet" href="https://fonts.googleapis.com/css2?family=EB+Garamond:ital,wght@0,400;0,600;0,700;0,800;1,400&display=swap">
<style>
  :root {
    --backdrop: #d6d6d6;
    --label-paper: #f5eadf;
    --trim: #f0cfae;
    --ink: #5f6062;
    --ink-soft: #6e6f72;
    --art-tone: #c9a98a;
    --ghost-tone: #ece0d3;
    --warning-rule: #efcfb2;
  }
  * { margin: 0; padding: 0; box-sizing: border-box; }
  html, body { width: 1200px; height: 1200px; overflow: hidden; }
  body {
    background: var(--backdrop);
    font-family: "EB Garamond", Georgia, serif;
    color: var(--ink);
    position: relative;
  }
  .label {
    position: absolute;
    left: 0; top: 232px;
    width: 1200px; height: 671px;
    background: var(--label-paper);
  }
  .trim-line {
    position: absolute; left: 0; width: 100%;
    height: 4px; background: var(--trim);
  }
  .trim-top-outer { top: 10px; }
  .trim-top-inner { top: 21px; height: 2px; }
  .trim-bottom-inner { bottom: 21px; height: 2px; }
  .trim-bottom-outer { bottom: 10px; }

  .front-panel, .back-panel { position: absolute; top: 0; height: 100%; text-align: center; }
  .front-panel { left: 0; width: 584px; }
  .back-panel { left: 620px; width: 484px; }

  .tagline {
    position: absolute; top: 53px; width: 100%;
    font-style: italic; font-size: 19px; color: var(--ink-soft);
  }
  .still-art {
    position: absolute; left: 222px; top: 120px;
    width: 126px; height: 146px;
    background: radial-gradient(ellipse at 50% 60%, var(--art-tone) 0%, #d9bda2 55%, var(--label-paper) 100%);
    border-radius: 8px;
  }
  .brand-name {
    position: absolute; top: 300px; width: 100%;
    font-weight: 800; font-size: 56px; letter-spacing: 1px;
    color: var(--ink-soft); line-height: 1;
  }
  .product-type {
    position: absolute; top: 372px; width: 100%;
    font-weight: 600; font-size: 32px; letter-spacing: 14px;
    padding-left: 14px; line-height: 1;
  }
  .source-line {
    position: absolute; top: 448px; width: 100%;
    font-style: italic; font-size: 19px; color: var(--ink-soft);
  }
  .strength {
    position: absolute; top: 515px; width: 100%;
    font-weight: 700; font-size: 22px;
  }
  .maker-line {
    position: absolute; top: 590px; width: 100%;
    font-weight: 700; font-size: 16px;
  }

  .ghost-art {
    position: absolute; left: 58px; top: 180px;
    width: 380px; height: 430px;
    background: radial-gradient(ellipse at 40% 60%, var(--ghost-tone) 0%, var(--label-paper) 70%);
  }
  .story {
    position: absolute; top: 71px; left: 0; width: 100%;
    font-size: 15.6px; line-height: 19px;
  }
  .bottler {
    position: absolute; top: 254px; left: 0; width: 100%;
    font-size: 15.6px; line-height: 19px;
  }
  .warning-box {
    position: absolute; left: 41px; top: 429px;
    width: 401px; height: 151px;
    border: 2px solid var(--warning-rule);
    padding: 18px 10px 0;
    font-size: 15.6px; line-height: 19px;
  }
</style>
</head>
<body>
  <section class="label">
    <div class="trim-line trim-top-outer"></div>
    <div class="trim-line trim-top-inner"></div>
    <div class="trim-line trim-bottom-inner"></div>
    <div class="trim-line trim-bottom-outer"></div>

    <div class="front-panel">
      <p class="tagline">Handmade with Natural Spring Water</p>
      <div class="still-art" role="img" aria-label="Engraved illustration of a copper pot still"></div>
      <h1 class="brand-name">LATE BIRCH</h1>
      <p class="product-type">VODKA</p>
      <p class="source-line">Distilled From Organic Cane Sugar</p>
      <p class="strength">40% abv</p>
      <p class="maker-line">Ferncliff Distillery Toronto, Canada</p>
    </div>

    <div class="back-panel">
      <div class="ghost-art" role="img" aria-label="Faint large illustration of a pot still"></div>
      <p class="story">
        Our vodka is handmade in small batches to the highest<br>
        standards befitting the true vodka perfectionist.<br>
        We use silk filtering process for exceptional purity, clarity,<br>
        and smoothness.<br>
        It is distilled 6 times from the finest organic cane sugar using<br>
        only the best Canadian spring water.<br>
        Discover the smooth, clear taste for yourself.
      </p>
      <p class="bottler">
        Distilled and Bottled by<br>
        Ferncliff Distillery Inc.<br>
        Toronto, Canada
      </p>
      <div class="warning-box">
        In accordance to the Surgeon General, women should<br>
        not drink alcoholic beverages during pregnancy because<br>
        of the risk of birth defects. Consumption of alcoholic<br>
        beverages impairs your ability to drive a car or operate<br>
        machinery and may cause health problems.
      </div>
    </div>
  </section>
</body>
</html>
```